5-star Hotel Web Design Project

I need a custom website design for a 5-star hotel. For full details please look at the attached ZIP archive.

The design should be in layers in Photoshop/Illustrator/InDesign format with all the icons/shapes/maps/graphic assets in vector format (svg, ai, eps) as much as possible.

I prefer white, simple but elegant websites. Please consider the performance/coding experience. We're not making something to show off our design skills on a design contest with fancy parallax effects and confusing animations. We're trying to create usable, functional and clean UI with good UX.

I would like to receive a few option for the color scheme to choose from.

The website will be custom coded, i.e. I'm not using WordPress.

NOTE: Don't bother to submit the generic WordPress style templates. We're looking for something custom made with attention to details. That's why the price is not guaranteed, but don't be mistaken, I'm a long time buyer here on SketchHive and all my projects are paid in full.

Low design quality

Europe

Hotel

5+ page

```html
<!DOCTYPE html>
<html lang="en">
<head>
<meta charset="utf-8">
<title>Coral Bay Resort – Summer Offer</title>
<link href="https://fonts.googleapis.com/css2?family=Poppins:wght@400;500;600&display=swap" rel="stylesheet">
<style>
:root{
  --navy:#0b1a33;
  --lavender:#e6e6f5;
  --crimson:#b0113a;
  --gold:#d6b262;
  --sky:#c9e6f5;
  --ink:#1a1a1a;
  --white:#ffffff;
  --grey-line:#3a3f5c;
}
*{margin:0;padding:0;box-sizing:border-box}
html,body{width:691px;height:1200px;overflow:hidden}
body{position:relative;background:var(--lavender);font-family:'Poppins',sans-serif;color:var(--ink)}
.abs{position:absolute}

/* header */
.site-header{position:absolute;left:0;top:0;width:691px;height:49px;background:var(--navy)}
.brand{left:54px;top:12px;width:70px;color:var(--crimson);font-size:9px;font-weight:500;line-height:11px;text-align:center}
.brand-dot{display:block;width:10px;height:10px;border-radius:50%;background:var(--crimson);margin:0 auto 2px}
.top-btn{top:3px;height:19px;background:var(--sky);border-radius:3px;color:var(--navy);font-size:7.5px;display:flex;align-items:center;justify-content:center;gap:4px}
.phone-btn{left:412px;width:92px}
.contact-btn{left:511px;width:59px}
.lang-btn{left:577px;width:60px}
.nav-rule{left:255px;top:27px;width:382px;height:1px;background:var(--gold)}
.main-nav{top:32px;left:0;width:691px;height:15px}
.main-nav a{position:absolute;top:0;height:15px;line-height:15px;color:var(--white);font-size:7.5px;font-weight:500;text-decoration:none;white-space:nowrap}
.main-nav a.is-active{background:var(--gold);color:var(--crimson);padding:0 9px;border-radius:1px}

/* section titles */
.section-title{left:0;width:691px;text-align:center;color:var(--crimson);font-size:12px;font-weight:500}
.title-rule{left:321px;width:49px;height:2px;background:var(--gold)}

/* offer card */
.offer-card{left:99px;top:110px;width:493px;height:599px;background:var(--white);border-radius:20px;box-shadow:0 1px 4px rgba(0,0,0,.12)}
.offer-heading{left:0;top:135px;width:691px;text-align:center;font-size:13px;color:var(--navy)}
.offer-text{left:173px;top:171px;width:345px;font-size:7.9px;line-height:12.3px;text-align:justify;text-indent:53px}
.offer-list{left:173px;top:253px;width:345px;list-style:none}
.offer-list li{position:relative;height:20.2px;padding-left:17px;font-size:7.9px;line-height:12px}
.offer-list li::before{content:"";position:absolute;left:1px;top:3px;width:6px;height:6px;border-radius:50%;background:#000}
.photo-frame{left:173px;top:369px;width:345px;height:148px;background:var(--white);box-shadow:0 0 3px rgba(0,0,0,.25)}
.resort-photo{left:178px;top:374px;width:335px;height:138px;border-radius:6px;background:linear-gradient(180deg,#7d9cc4 0%,#c3cfdc 35%,#d8d2c0 55%,#b9ad92 70%,#6a8ea3 78%,#4d7490 100%)}
.price-caption{left:0;top:541px;width:691px;text-align:center;font-size:9.5px;color:var(--navy)}
.price-table{left:173px;top:556px;width:345px;border-collapse:collapse;font-size:7.5px;color:var(--navy)}
.price-table th,.price-table td{border:1px solid var(--grey-line);height:14.8px;text-align:center;font-weight:500;padding:0}
.price-table td{font-weight:400}
.price-table th:first-child{width:49px}
.book-btn{left:308px;top:668px;width:75px;height:20px;background:var(--crimson);color:var(--gold);border-radius:4px;font-size:9.5px;font-weight:500;display:flex;align-items:center;justify-content:center}

/* explore cards */
.offer-tile{top:771px;width:147px;height:189px;background:var(--white);border-radius:6px}
.tile-photo{position:absolute;left:6px;top:6px;width:135px;height:89px;border-radius:6px}
.tile-title{position:absolute;left:0;top:102px;width:147px;text-align:center;font-size:8px;font-weight:500;color:#111}
.tile-text{position:absolute;left:5px;top:119px;width:137px;text-align:center;font-size:6.4px;line-height:10.3px;color:#333}
.tile-btn{position:absolute;left:42px;top:159px;width:63px;height:21px;background:var(--navy);color:var(--white);border-radius:4px;font-size:8px;display:flex;align-items:center;justify-content:center}
.photo-night{background:linear-gradient(160deg,#2a2412 0%,#6b5323 40%,#243a2a 70%,#1c4a6a 100%)}
.photo-snow{background:linear-gradient(170deg,#7a7d80 0%,#d9dadb 35%,#c4c7c5 60%,#3f4d45 100%)}
.photo-sea{background:linear-gradient(180deg,#a9c3dc 0%,#6ea3c2 40%,#2f7fa3 65%,#d9c9b8 100%)}
.carousel-arrow{top:855px}
.dots{top:981px;left:0;width:691px;height:10px}

/* footer */
.site-footer{left:0;top:1002px;width:691px;height:198px;background:var(--navy);border-top:1px solid #5a5f7a}
.footer-title{left:54px;top:1014px;color:var(--white);font-size:11px;font-weight:600}
.footer-links a{position:absolute;color:var(--white);font-size:11.5px;text-decoration:none;white-space:nowrap}
.footer-brand{left:480px;top:1060px;width:156px;text-align:center;color:var(--crimson);font-size:17px;font-weight:500;line-height:20px}
.footer-brand-dot{display:block;width:22px;height:22px;border-radius:50%;background:var(--crimson);margin:0 auto 6px}
.social{left:479px;top:1140px;width:160px;height:24px;display:flex;gap:2.5px}
.social span{width:24px;height:24px;border-radius:50%;background:#2f6fb8}
.stay{left:480px;top:1170px;width:156px;text-align:center;color:var(--white);font-size:12px}
</style>
</head>
<body>

<header class="site-header">
  <div class="abs brand"><span class="brand-dot"></span>Coral Bay Resort</div>
  <div class="abs top-btn phone-btn">
    <svg width="10" height="10" viewBox="0 0 24 24"><path fill="#0b1a33" d="M6.6 10.8a15 15 0 0 0 6.6 6.6l2.2-2.2a1 1 0 0 1 1-.25 11 11 0 0 0 3.6.6 1 1 0 0 1 1 1V20a1 1 0 0 1-1 1A17 17 0 0 1 3 4a1 1 0 0 1 1-1h3.5a1 1 0 0 1 1 1c0 1.25.2 2.45.6 3.6a1 1 0 0 1-.25 1z"/></svg>
    +359 500 410 77
  </div>
  <div class="abs top-btn contact-btn">CONTACT</div>
  <div class="abs top-btn lang-btn">ENGLISH
    <svg width="8" height="5" viewBox="0 0 8 5"><path d="M0 0h8L4 5z" fill="#b0113a"/></svg>
  </div>
  <div class="abs nav-rule"></div>
  <nav class="abs main-nav">
    <a style="left:265px">HOME</a>
    <a style="left:319px">CORAL BAY</a>
    <a style="left:415px">BOOK DIRECT</a>
    <a class="is-active" style="left:492px">SPECIAL OFFERS</a>
    <a style="left:597px">LOCATION</a>
  </nav>
</header>

<h1 class="abs section-title" style="top:74px">Offer Details</h1>
<div class="abs title-rule" style="top:93px"></div>

<section class="abs offer-card"></section>
<h2 class="abs offer-heading" style="font-weight:400">SUMMER OFFER</h2>
<p class="abs offer-text">Lorem ipsum dolor sit amet, consectetur adipiscing elit. Nulla efficitur interdum nunc vitae tincidunt. Vestibulum porttitor tortor id eros feugiat, at ullamcorper est lobortis. Nunc semper orci a pellentesque porta. Interdum et malesuada fames ac ante ipsum primis in faucibus. Maecenas sit amet sollicitudin sem. Nulla non rutrum nisl. Proin tincidunt leo et odio luctus, ac pulvinar ligula vehicula. Integer est elit, posuere sed quam ut</p>
<ul class="abs offer-list">
  <li>Lorem ipsum dolor sit amet, consectetur adipiscing elit. Nulla efficitur</li>
  <li>Lorem ipsum dolor sit amet, consectetur adipiscing elit. Nulla efficitur</li>
  <li>Lorem ipsum dolor sit amet, consectetur adipiscing elit. Nulla efficitur</li>
  <li>Lorem ipsum dolor sit amet, consectetur adipiscing elit. Nulla efficitur</li>
  <li>Lorem ipsum dolor sit amet, consectetur adipiscing elit. Nulla efficitur</li>
</ul>
<div class="abs photo-frame"></div>
<div class="abs resort-photo" role="img" aria-label="Resort buildings along a sandy beach under a cloudy sky"></div>

<div class="abs price-caption">PRICE TABLE</div>
<table class="abs price-table">
  <tr><th></th><th>May</th><th>June</th><th>July</th><th>August</th><th>September</th></tr>
  <tr><th>Studio</th><td>€ XX</td><td>€ XX</td><td>€ XX</td><td>€ XX</td><td>€ XX</td></tr>
  <tr><th>A1</th><td>€ XX</td><td>€ XX</td><td>€ XX</td><td>€ XX</td><td>€ XX</td></tr>
  <tr><th>A2</th><td>€ XX</td><td>€ XX</td><td>€ XX</td><td>€ XX</td><td>€ XX</td></tr>
  <tr><th>A3</th><td>€ XX</td><td>€ XX</td><td>€ XX</td><td>€ XX</td><td>€ XX</td></tr>
  <tr><th>Villa</th><td>€ XX</td><td>€ XX</td><td>€ XX</td><td>€ XX</td><td>€ XX</td></tr>
</table>
<div class="abs book-btn">BOOK NOW</div>

<h2 class="abs section-title" style="top:727px">Explore More</h2>
<div class="abs title-rule" style="top:746px"></div>

<svg class="abs carousel-arrow" style="left:59px" width="31" height="31" viewBox="0 0 31 31"><circle cx="15.5" cy="15.5" r="14" fill="#fff" stroke="#0b1a33" stroke-width="2.5"/><circle cx="15.5" cy="15.5" r="10.5" fill="none" stroke="#0b1a33" stroke-width="1.5"/><path d="M21 15.5H10M14.5 11l-4.5 4.5 4.5 4.5" fill="none" stroke="#0b1a33" stroke-width="2"/></svg>
<svg class="abs carousel-arrow" style="left:602px" width="31" height="31" viewBox="0 0 31 31"><circle cx="15.5" cy="15.5" r="14" fill="#fff" stroke="#0b1a33" stroke-width="2.5"/><circle cx="15.5" cy="15.5" r="10.5" fill="none" stroke="#0b1a33" stroke-width="1.5"/><path d="M10 15.5h11M16.5 11l4.5 4.5-4.5 4.5" fill="none" stroke="#0b1a33" stroke-width="2"/></svg>

<article class="abs offer-tile" style="left:98px">
  <div class="tile-photo photo-night" role="img" aria-label="Resort lit up at night with pools"></div>
  <div class="tile-title">New Year Offer</div>
  <p class="tile-text">Lorem ipsum dolor sit amet, consectetur adipiscing elit, sed do eiusmod tempor incididunt ut labore et dolore magna</p>
  <div class="tile-btn">View Details</div>
</article>
<article class="abs offer-tile" style="left:272px">
  <div class="tile-photo photo-snow" role="img" aria-label="Aerial view of the resort covered in snow"></div>
  <div class="tile-title">Chrismass Offer</div>
  <p class="tile-text">Lorem ipsum dolor sit amet, consectetur adipiscing elit, sed do eiusmod tempor incididunt ut labore et dolore magna</p>
  <div class="tile-btn">View Details</div>
</article>
<article class="abs offer-tile" style="left:446px">
  <div class="tile-photo photo-sea" role="img" aria-label="Guest relaxing on a sailboat at sea"></div>
  <div class="tile-title">Special offer - 50%</div>
  <p class="tile-text">Lorem ipsum dolor sit amet, consectetur adipiscing elit, sed do eiusmod tempor incididunt ut labore et dolore magna</p>
  <div class="tile-btn">View Details</div>
</article>

<svg class="abs dots" viewBox="0 0 691 10">
  <circle cx="320" cy="5" r="3.8" fill="#b5a9a9"/>
  <circle cx="333" cy="5" r="4.6" fill="#d6b262" stroke="#7a6220" stroke-width=".8"/>
  <circle cx="346" cy="5" r="4.6" fill="#d6b262" stroke="#7a6220" stroke-width=".8"/>
  <circle cx="359" cy="5" r="4.6" fill="#d6b262" stroke="#7a6220" stroke-width=".8"/>
  <circle cx="372" cy="5" r="3.8" fill="#b5a9a9"/>
</svg>

<footer class="abs site-footer"></footer>
<div class="abs footer-title">QUICK NAVIGATION</div>
<nav class="footer-links">
  <a style="left:54px;top:1049px">Contact</a>
  <a style="left:54px;top:1078px">Brochure</a>
  <a style="left:54px;top:1108px">Company Details</a>
  <a style="left:54px;top:1140px">Hotel Fact Sheet</a>
  <a style="left:54px;top:1169px">Stay Safe Organizer</a>
  <a style="left:188px;top:1049px">Awards</a>
  <a style="left:187px;top:1078px">Prices</a>
  <a style="left:187px;top:1108px">360® VR</a>
  <a style="left:187px;top:1140px">FAQ</a>
  <a style="left:327px;top:1049px">Terms</a>
  <a style="left:326px;top:1078px">Disclaimer</a>
  <a style="left:326px;top:1108px">Privacy Policy</a>
</nav>
<div class="abs footer-brand"><span class="footer-brand-dot"></span>Coral Bay Resort</div>
<div class="abs social"><span></span><span></span><span></span><span></span><span></span><span></span></div>
<div class="abs stay">Stay Connected</div>

</body>
</html>
```